Create Brisk Lesson Studio a card design that will stick in the mind of prospects.

Brisk Lesson Studio specialises designs and produces training video, animation, illustration and text.

We need a card design that oozes class and leaves the prospect brimming with confidence.

The design will feature the Brisk Lesson Studio all black logo (uploaded). The design may also use the shade of orange from the orange version of the logo (uploaded). Note, just the color is to be used e.g. for the back of the card, not the orange logo itself.

The Brisk brand is about authenticity, quality, maturity and assurance. We are a safe buy when it comes to the prospects next project.

Target Market(s)

The primary target is training managers or others who are responsible for choosing to hire companies to produce their training media e.g. video. This will usually be a large spend so they need to have confidence.

Industry/Entity Type

Training

Contact Information for Business Card

FRONT:

Brisk Lesson Studio
Phone: 03 5172 4039
1st Floor, 418 Kellerby Road
Mt Ferncombe
VIC 3862
Australia
www.brisklesson.com.au

Lionel Petch
Founder and Lead Consultant
mobile: +61 3 0462 735 218
email: lionel@brisklesson.com.au

BACK:
Specialising in design and production of training:

video
animation
illustration
text

for delivery via internet, intranet and/or LMS.

Number of Pages Required

4 page

Font styles to use
Sans Serif

Requirements
Must have
• The black logo uploaded with the brief.
Nice to have
• The inclusion of the shade of orange found in the orange logo also uploaded with the brief. One example would be having the back of the card in this orange and using a white font for the text. But I want the designer to work this out.
Should not have
• No colours other than black and the orange included in the uploaded orange logo.

```html
<!DOCTYPE html>
<html lang="en">
<head>
<meta charset="utf-8">
<title>Brisk Lesson Studio — Business Card</title>
<link rel="stylesheet" href="https://fonts.googleapis.com/css2?family=Open+Sans:wght@400;600&display=swap">
<style>
  :root {
    --orange: #e5601c;
    --orange-light: #ee7a2c;
    --orange-dark: #cf4f14;
    --ink: #1e1e1e;
    --grey: #6b6b6b;
    --rule: #bdbdbd;
    --paper: #ffffff;
    --backdrop: #ece8e2;
  }
  * { box-sizing: border-box; margin: 0; padding: 0; }
  html, body {
    width: 1200px; height: 780px; overflow: hidden;
    background: var(--backdrop);
    font-family: "Open Sans", Arial, sans-serif;
  }
  .stage {
    width: 1200px; height: 780px;
    display: flex; justify-content: center; align-items: center; gap: 90px;
  }
  .card {
    width: 390px; height: 620px;
    border-radius: 26px;
    overflow: hidden;
    position: relative;
    box-shadow: 0 10px 30px rgba(0,0,0,0.18);
  }

  /* Front */
  .card-front { background: var(--paper); display: flex; flex-direction: column; }
  .front-body { flex: 1; padding: 46px 34px 0; text-align: center; }
  .wordmark {
    display: flex; align-items: center; justify-content: center; gap: 14px;
    margin-bottom: 36px;
  }
  .wordmark-dot { width: 22px; height: 22px; border-radius: 50%; background: currentColor; }
  .wordmark-name { font-size: 64px; font-weight: 600; line-height: 1; }
  .wordmark--orange { color: var(--orange); }
  .wordmark--black { color: var(--ink); }

  .company-name { color: var(--orange); font-size: 27px; font-weight: 400; margin-bottom: 12px; }
  .address { color: var(--grey); font-size: 17px; line-height: 1.45; }
  .contact-line {
    display: flex; align-items: center; justify-content: center; gap: 10px;
    color: var(--grey); font-size: 17px; margin-top: 8px;
  }
  .icon {
    width: 26px; height: 22px; border-radius: 5px; background: var(--orange);
    display: inline-flex; align-items: center; justify-content: center; flex: none;
  }
  .divider { border: 0; border-top: 1px solid var(--rule); margin: 26px 10px 22px; }
  .person-name { color: var(--orange); font-size: 24px; font-weight: 400; }
  .person-role { color: var(--grey); font-size: 17px; margin: 4px 0 6px; }
  .contact-list { display: flex; flex-direction: column; align-items: flex-start; padding-left: 28px; }
  .contact-list .contact-line { justify-content: flex-start; }

  .front-band {
    height: 82px; background: var(--orange);
    display: flex; align-items: center; justify-content: center;
    color: var(--paper); font-size: 19px; letter-spacing: 0.3px;
  }

  /* Back */
  .card-back {
    background: radial-gradient(circle at 45% 40%, var(--orange-light), var(--orange) 55%, var(--orange-dark));
    color: var(--ink);
    text-align: center;
    padding: 110px 30px 0;
  }
  .card-back .wordmark { margin-bottom: 56px; }
  .card-back .wordmark-name { font-size: 70px; }
  .back-intro { font-size: 19px; line-height: 1.3; margin-bottom: 22px; }
  .service-list { list-style: none; font-size: 20px; line-height: 1.15; margin-bottom: 40px; }
  .back-outro { font-size: 19px; line-height: 1.3; }
</style>
</head>
<body>
<main class="stage">

  <section class="card card-front" aria-label="Card front">
    <div class="front-body">
      <div class="wordmark wordmark--orange">
        <span class="wordmark-dot"></span>
        <span class="wordmark-name">Brisk</span>
      </div>

      <h1 class="company-name">Brisk Lesson Studio</h1>
      <p class="address">1st Floor, 418 Kellerby Road<br>Mt Ferncombe, VIC 3862, Australia</p>
      <p class="contact-line">
        <span class="icon"><svg width="14" height="14" viewBox="0 0 24 24" fill="#fff"><path d="M6.6 10.8a15.1 15.1 0 0 0 6.6 6.6l2.2-2.2a1 1 0 0 1 1-.25 11.4 11.4 0 0 0 3.6.57 1 1 0 0 1 1 1V20a1 1 0 0 1-1 1A17 17 0 0 1 3 4a1 1 0 0 1 1-1h3.5a1 1 0 0 1 1 1c0 1.25.2 2.45.57 3.57a1 1 0 0 1-.25 1z"/></svg></span>
        03 5172 4039
      </p>

      <hr class="divider">

      <h2 class="person-name">Lionel Petch</h2>
      <p class="person-role">Founder and Lead Consultant</p>
      <div class="contact-list">
        <p class="contact-line">
          <span class="icon"><svg width="12" height="15" viewBox="0 0 12 16" fill="none" stroke="#fff" stroke-width="1.6"><rect x="1.5" y="1" width="9" height="14" rx="1.5"/><line x1="4.5" y1="12.5" x2="7.5" y2="12.5"/></svg></span>
          +61 3 0462 735 218
        </p>
        <p class="contact-line">
          <span class="icon"><svg width="16" height="12" viewBox="0 0 16 12" fill="none" stroke="#fff" stroke-width="1.5"><rect x="1" y="1" width="14" height="10" rx="1"/><path d="M1 1l7 6 7-6"/></svg></span>
          lionel@brisklesson.com.au
        </p>
      </div>
    </div>
    <footer class="front-band">www.brisklesson.com.au</footer>
  </section>

  <section class="card card-back" aria-label="Card back">
    <div class="wordmark wordmark--black">
      <span class="wordmark-dot"></span>
      <span class="wordmark-name">Brisk</span>
    </div>
    <p class="back-intro">Specialising in design and<br>production of training:</p>
    <ul class="service-list">
      <li>video</li>
      <li>animation</li>
      <li>illustration</li>
      <li>text</li>
    </ul>
    <p class="back-outro">for delivery via internet<br>intranet and/or LMS.</p>
  </section>

</main>
</body>
</html>
```